RTV Photography Business Card Design

I would like a business card designed in the shape of a camera.
Would like to see various camera designs. Would like to see what the card looks like in different colors. Would like to see which logo looks better on the various camera designs so please show me some with the white logo and some with the black logo. If you need a different file formats please let me know.
Project Deadline Extended Reason: My grandfather passed away and dealing with funeral plans so need to extend deadline. Added Tuesday, March 1, 2016
Project Deadline Extended
Reason: I just got back from out of town. My grandfather's passing was the primary focus for me these past few weeks and the funeral is over so now I will concentrate on picking my business card design. I really appreciate each designer who has taken the time to submit a design. Your effort has not gone unnoticed. I look forward to seeing more amazing designs.
Industry/Entity Type
Business
Contact Information for Business Card
Wren
757-418-2096
https://www.facebook.com/rtvphotographyfreelance/
DoraWren@rtv-photography.example
Look and feel

```html
<!DOCTYPE html>
<html lang="en">
<head>
<meta charset="utf-8">
<title>RTV Photography – Business Card</title>
<link href="https://fonts.googleapis.com/css2?family=Fira+Sans:wght@400;500&family=Fira+Sans+Condensed:wght@700&display=swap" rel="stylesheet">
<style>
  :root {
    --backdrop: #9fae6f;
    --card: #000000;
    --gold: #c9a02a;
    --gold-soft: #b8942c;
    --divider: #3a3a3a;
  }
  html, body {
    margin: 0;
    padding: 0;
    width: 1200px;
    height: 1200px;
    overflow: hidden;
    background: var(--backdrop);
  }
  .canvas {
    position: relative;
    width: 1200px;
    height: 1200px;
  }
  .card-shape {
    position: absolute;
    inset: 0;
  }
  .brand {
    position: absolute;
    left: 130px;
    top: 640px;
    width: 400px;
    display: flex;
    align-items: center;
    justify-content: center;
    gap: 14px;
    font-family: "Fira Sans", sans-serif;
    font-weight: 500;
    font-size: 30px;
    letter-spacing: 2px;
    color: var(--gold);
  }
  .brand-dot {
    width: 26px;
    height: 26px;
    border-radius: 50%;
    background: var(--gold);
    flex: none;
  }
  .details {
    position: absolute;
    left: 620px;
    top: 570px;
    color: var(--gold);
    font-family: "Fira Sans", sans-serif;
  }
  .person-name {
    margin: 0;
    font-family: "Fira Sans Condensed", sans-serif;
    font-weight: 700;
    font-size: 40px;
    font-variant: small-caps;
    letter-spacing: 1px;
    line-height: 1;
  }
  .person-role {
    margin: 8px 0 0;
    font-size: 28px;
    color: var(--gold-soft);
  }
  .contact-list {
    list-style: none;
    margin: 95px 0 0;
    padding: 0;
    font-size: 29px;
  }
  .contact-list li {
    display: flex;
    align-items: center;
    gap: 18px;
    margin-bottom: 8px;
  }
  .contact-icon {
    width: 24px;
    height: 24px;
    flex: none;
  }
</style>
</head>
<body>
<div class="canvas">
  <svg class="card-shape" width="1200" height="1200" viewBox="0 0 1200 1200" aria-hidden="true">
    <path class="camera-body" fill="var(--card)"
      d="M80,400 L330,400 L370,310 L660,310 L700,400 L1120,400 L1150,430 L1150,930 L1120,960 L80,960 L50,930 L50,430 Z"/>
    <circle class="viewfinder-hole" cx="1010" cy="475" r="38" fill="var(--backdrop)"/>
    <circle class="lens-ring" cx="330" cy="680" r="210" fill="none" stroke="var(--backdrop)" stroke-width="9"
      stroke-dasharray="309.9 20" transform="rotate(-85 330 680)"/>
    <line class="divider" x1="560" y1="560" x2="566" y2="900" stroke="var(--divider)" stroke-width="4"/>
  </svg>

  <div class="brand">
    <span class="brand-dot"></span>
    <span class="brand-name">RTV PHOTOGRAPHY</span>
  </div>

  <div class="details">
    <h1 class="person-name">Your Name</h1>
    <p class="person-role">Designation</p>
    <ul class="contact-list">
      <li>
        <svg class="contact-icon" viewBox="0 0 24 24" fill="var(--gold)"><path d="M3 8c3-3 15-3 18 0l-1 3-4-1V8H8v2l-4 1z"/><path d="M7 12h10l3 7H4z"/></svg>
        <span>123-456-789</span>
      </li>
      <li>
        <svg class="contact-icon" viewBox="0 0 24 24" fill="none" stroke="var(--gold)" stroke-width="2"><circle cx="12" cy="12" r="9"/><ellipse cx="12" cy="12" rx="4" ry="9"/><line x1="3" y1="12" x2="21" y2="12"/></svg>
        <span>website.com</span>
      </li>
      <li>
        <svg class="contact-icon" viewBox="0 0 24 24" fill="none" stroke="var(--gold)" stroke-width="2"><rect x="3" y="6" width="18" height="12"/><path d="M3 6l9 7 9-7"/></svg>
        <span>emailid@youremail.com</span>
      </li>
    </ul>
  </div>
</div>
</body>
</html>
```